Brightfold websites redesign

Www.bright-fold.com needs to be redesigned along with updations. The incremental material will be provided for the updations. We are looking for complete redesign of the pages with the new content. The complete write up will be provided soon

Target Market(s)

Global

Coding

Coded - Design and coding required

Number of Pages Required

5+ page

Requirements
Must have
• A clean and slick design for the Consulting.
Should not have
• Too many pictures which reduces the speed of the site

```html
<!DOCTYPE html>
<html lang="en">
<head>
<meta charset="utf-8">
<title>Brightfold Consultancy</title>
<link rel="stylesheet" href="https://fonts.googleapis.com/css2?family=Ubuntu:wght@400;500&family=Open+Sans:wght@400;600&display=swap">
<style>
:root{
  --navy:#283852;
  --navy-deep:#223049;
  --blue:#3aa0cd;
  --blue-dark:#2a88b6;
  --band:#3ca4d0;
  --ink:#2c2c34;
  --body:#666a72;
  --line:#e1e3e6;
  --white:#ffffff;
}
*{margin:0;padding:0;box-sizing:border-box}
html,body{width:742px;height:1200px;overflow:hidden;background:var(--white)}
body{position:relative;font-family:"Open Sans",Arial,sans-serif;color:var(--body)}
.abs{position:absolute}
h1,h2,h3{font-family:"Ubuntu",Arial,sans-serif;font-weight:400;color:var(--ink)}

/* header */
.site-header{left:0;top:0;width:742px;height:66px;background:var(--navy)}
.brand{left:69px;top:0;width:169px;height:66px;background:var(--white);display:flex;align-items:center;justify-content:center;gap:7px}
.brand-dot{width:14px;height:14px;border-radius:50%;background:var(--blue)}
.brand-name{font-family:"Ubuntu",sans-serif;font-size:18px;color:var(--navy)}
.nav-item{top:0;height:66px;line-height:66px;font-size:7.5px;color:var(--white);letter-spacing:.2px}
.nav-item.active{background:var(--blue);text-align:center;width:52px}

/* hero */
.hero{left:0;top:66px;width:742px;height:306px;
  background:
    radial-gradient(circle at 580px 165px,rgba(150,185,215,.95) 0,rgba(120,160,200,.85) 70px,rgba(170,200,225,.55) 105px,rgba(205,220,234,0) 125px),
    linear-gradient(100deg,#c9d6e2 0%,#dfe7ef 45%,#d3deea 70%,#b8cadc 100%)}
.hero-title{left:69px;top:188px;font-size:19.5px;color:var(--navy);letter-spacing:.2px}
.hero-text{left:69px;top:221px;width:350px;font-size:7.2px;line-height:16px;color:#2f3540}
.hero-arrow{top:262px;width:14px;height:14px;border-radius:50%}

/* cards */
.card{top:394px;width:177px;height:242px;background:var(--white);box-shadow:0 0 6px rgba(0,0,0,.13)}
.card-photo{position:absolute;left:9px;top:9px;width:158px;height:90px;border:2px solid #fff;box-shadow:0 0 3px rgba(0,0,0,.25)}
.card-title{position:absolute;left:9px;top:113px;font-size:13px;color:var(--navy)}
.card-text{position:absolute;left:9px;top:137px;width:160px;font-size:7px;line-height:18px;text-align:justify}
.card-btn{position:absolute;left:0;bottom:0;width:177px;height:34px;background:linear-gradient(var(--blue),var(--blue-dark));color:var(--white);font-family:"Ubuntu",sans-serif;font-size:9.5px;font-weight:500;line-height:34px;padding-left:11px}
.card-btn span{position:absolute;right:12px;font-size:11px}

/* welcome */
.welcome-title{left:69px;top:665px;font-size:16px;color:var(--ink)}
.welcome-text{left:69px;top:690px;width:388px;font-size:6.7px;line-height:19px;text-align:justify;letter-spacing:-.05px}
.divider{left:69px;top:879px;width:397px;height:3px;background:var(--line)}
.trade-badge{left:69px;top:899px;width:73px;height:73px;border-radius:50%;background:radial-gradient(circle at 45% 45%,#e6f1f6 0,#bcd9e6 14px,#3a9ec4 16px,#1f6f93 100%)}
.trade-title{left:154px;top:900px;font-size:13px;color:var(--ink)}
.trade-text{left:154px;top:921px;width:312px;font-size:7px;line-height:19px}

/* contact */
.contact{left:482px;top:669px;width:190px;height:311px;background:var(--navy);box-shadow:0 6px 6px -3px rgba(0,0,0,.3)}
.contact-title{position:absolute;left:14px;top:14px;font-size:16px;color:var(--white)}
.contact-rule{position:absolute;left:14px;top:39px;width:158px;height:1px;background:#6d7d97}
.field{position:absolute;left:16px;width:156px;background:var(--white);font-size:7px;color:#7a7f87;padding:11px 10px}
.field svg{position:absolute;right:9px;top:11px}
.submit{position:absolute;left:48px;top:253px;width:94px;height:32px;background:linear-gradient(var(--blue),var(--blue-dark));color:var(--white);font-family:"Ubuntu",sans-serif;font-size:9.5px;font-weight:500;text-align:center;line-height:32px}

/* band */
.band{left:0;top:1014px;width:742px;height:138px;background:var(--band)}
.band-title{font-size:13px;color:var(--white)}
.dot{top:1049px;width:7px;height:7px;border-radius:50%;background:#7cc4e2}
.dot.on{background:var(--white)}
.avatar{left:70px;top:1070px;width:60px;height:60px;border-radius:50%;border:3px solid var(--white);background:linear-gradient(180deg,#f2f2f2 0,#e8e8e8 40%,#3b2f33 62%,#2a2428 100%)}
.quote-name{left:140px;top:1067px;font-family:"Ubuntu",sans-serif;font-size:9.5px;font-weight:500;color:var(--white)}
.quote-text{left:140px;top:1085px;width:280px;font-size:6.5px;line-height:16px;color:#eaf6fb}
.link{font-size:6.5px;color:var(--white)}

/* footer */
.site-footer{left:0;top:1152px;width:742px;height:48px;background:var(--navy-deep)}
.copyright{left:70px;top:1170px;font-size:7px;color:#d5dae2}
.social{top:1166px;width:18px;height:18px;border-radius:50%;background:var(--blue)}
</style>
</head>
<body>

<header class="abs site-header"></header>
<div class="abs brand"><span class="brand-dot"></span><span class="brand-name">Brightfold</span></div>
<nav>
  <div class="abs nav-item active" style="left:278px">HOME</div>
  <div class="abs nav-item" style="left:346px">FOUNDER</div>
  <div class="abs nav-item" style="left:410px">CONSULTANCY</div>
  <div class="abs nav-item" style="left:495px">SYSTEM</div>
  <div class="abs nav-item" style="left:555px">CASE STUDIES</div>
  <div class="abs nav-item" style="left:638px">CONTACT</div>
</nav>

<section class="abs hero" role="img" aria-label="Glass globe resting on financial documents in pale blue tones"></section>
<h1 class="abs hero-title">STRUCTURED FINANCING SOLUTIONS</h1>
<p class="abs hero-text">The Consultancy provides end-to-end structured solutions on the Payables, Receivables or Inventory side for working capital requirements with off/part/on recourse balance sheet structures.</p>
<svg class="abs hero-arrow" style="left:69px" viewBox="0 0 14 14"><circle cx="7" cy="7" r="7" fill="#2d3440"/><path d="M8.2 4 5.2 7l3 3" stroke="#fff" stroke-width="1.6" fill="none"/></svg>
<svg class="abs hero-arrow" style="left:87px" viewBox="0 0 14 14"><circle cx="7" cy="7" r="7" fill="#3aa0cd"/><path d="M5.8 4 8.8 7l-3 3" stroke="#fff" stroke-width="1.6" fill="none"/></svg>

<article class="abs card" style="left:69px">
  <div class="card-photo" role="img" aria-label="Business people reviewing charts on a tablet" style="background:linear-gradient(160deg,#d8d4ce 0%,#b9b2a9 40%,#5b4a3e 75%,#3a2e27 100%)"></div>
  <h2 class="card-title">OUR EXPERTISE</h2>
  <p class="card-text">BCL will work with you to understand your business and offer need based strategic and transactional advice which fits...</p>
  <div class="card-btn">READ MORE<span>»</span></div>
</article>
<article class="abs card" style="left:282px">
  <div class="card-photo" role="img" aria-label="Hands typing on a laptop beside printed charts" style="background:linear-gradient(135deg,#f1f2f3 0%,#d9dcdf 45%,#a7abb0 75%,#6e7278 100%)"></div>
  <h2 class="card-title">STRUCTURED FINANCING</h2>
  <p class="card-text">Lorem ipsum dolor sit amet, consectetur adip iscing elit. Cras non velit eu augue volu tpat tempor ut a velit.</p>
  <div class="card-btn">READ MORE<span>»</span></div>
</article>
<article class="abs card" style="left:495px">
  <div class="card-photo" role="img" aria-label="Team of colleagues in a meeting" style="background:linear-gradient(90deg,#8d9197 0%,#c9c4b6 35%,#d9d58f 55%,#b8bcc0 75%,#4e5358 100%)"></div>
  <h2 class="card-title">BANK LINES BUSINESS</h2>
  <p class="card-text">Lorem ipsum dolor sit amet, consectetur adip iscing elit. Cras non velit eu augue volu tpat tempor ut a velit.</p>
  <div class="card-btn">READ MORE<span>»</span></div>
</article>

<h2 class="abs welcome-title">WELCOME TO BRIGHTFOLD CONSULTANCY</h2>
<div class="abs welcome-text">
  <p>Brightfold Consultancy Limited capitalizes on synergies arising from trade and investment linkages between countries and knowledge of traditional and non-traditional pools of liquidity to provide consultancy services to Emerging country banks, Corporates and SMEs.</p>
  <p>The Consultancy provides bank neutral views to Corporates and SMEs in Asian emerging markets and helps in improving financial structure and efficient use of funds. Our endeavor is to provide a distinct bottom line advantage to our clients. The primary focus is in regionalisation of the banking relationship across the globe, providing structured finance solutions and off balance sheet solutions.</p>
  <p>The consultancy for the Banks and Non Banking Financial Institutions is focused on risk mitigation techniques, Export Credit Agency business and trade origination and distribution strategies along with raising long term liabilities.</p>
</div>
<div class="abs divider"></div>
<div class="abs trade-badge" role="img" aria-label="White world map on a blue circle"></div>
<h3 class="abs trade-title">WORLD MERCHANDISING TRADE 2012</h3>
<p class="abs trade-text">Duis ligula metus, ornare vitae risus vitae, laoreet consequat felis. Suspendisse turpis enim, cursus a hendrerit nec, sollicitudin non lorem. Nunc fermentum lorem nec congue soll icitudin. Sed pretium pharetra convallis.</p>

<aside class="abs contact">
  <h2 class="contact-title">QUICK CONTACT</h2>
  <div class="contact-rule"></div>
  <div class="field" style="top:56px;height:30px">Name<svg width="7" height="7" viewBox="0 0 8 8"><circle cx="4" cy="2.2" r="2" fill="#888"/><path d="M0 8c0-3 8-3 8 0z" fill="#888"/></svg></div>
  <div class="field" style="top:97px;height:30px">Phone<svg width="7" height="7" viewBox="0 0 8 8"><path d="M1 0h2l1 2-1 1c.6 1.2 1.3 1.9 2 2l1-1 2 1v2C4 8 0 4 1 0z" fill="#888"/></svg></div>
  <div class="field" style="top:140px;height:30px">Email Address<svg width="8" height="6" viewBox="0 0 8 6"><rect width="8" height="6" fill="#888"/><path d="M0 0l4 3 4-3" stroke="#fff" stroke-width=".8" fill="none"/></svg></div>
  <div class="field" style="top:182px;height:55px">Message<svg width="8" height="7" viewBox="0 0 8 7"><ellipse cx="4" cy="3" rx="4" ry="3" fill="#888"/><path d="M1 5 0 7l3-1.5z" fill="#888"/></svg></div>
  <div class="submit">SUBMIT</div>
</aside>

<section class="abs band"></section>
<h3 class="abs band-title" style="left:70px;top:1043px">TESTIMONIALS</h3>
<span class="abs dot" style="left:387px"></span>
<span class="abs dot on" style="left:398px"></span>
<span class="abs dot" style="left:409px"></span>
<div class="abs avatar" role="img" aria-label="Portrait of the client giving the testimonial"></div>
<div class="abs quote-name">John Joe.., Location</div>
<p class="abs quote-text">Ut wisi enim ad minim veniam, quis nostrud exerci tation ullamcorper suscipit lobortis nisl ut aliquip ex ea commodo consequat. Duis autem vel eum iriure dolor in hendrerit in vulp utate velit esse molestie consequat, vel illum dolore eu feugiat.</p>
<h3 class="abs band-title" style="left:459px;top:1043px">QUICK LINKS</h3>
<div class="abs link" style="left:460px;top:1073px">SERVICES</div>
<div class="abs link" style="left:460px;top:1092px">FOUNDER</div>
<div class="abs link" style="left:460px;top:1111px">ABOUT US</div>
<div class="abs link" style="left:541px;top:1073px">LOCATIONS</div>
<div class="abs link" style="left:541px;top:1092px">FAQ</div>
<div class="abs link" style="left:541px;top:1111px">MEDIA</div>
<div class="abs link" style="left:604px;top:1073px">CONTACT US</div>
<div class="abs link" style="left:604px;top:1092px">PRIVACY POLICY</div>
<div class="abs link" style="left:604px;top:1111px">SITEMAP</div>

<footer class="abs site-footer"></footer>
<p class="abs copyright">Copyrights@2016 Brightfold Consultancy Limited. All Right Reserved.</p>
<span class="abs social" style="left:591px" aria-label="Social link"></span>
<span class="abs social" style="left:612px" aria-label="Social link"></span>
<span class="abs social" style="left:634px" aria-label="Social link"></span>
<span class="abs social" style="left:655px" aria-label="Social link"></span>

</body>
</html>
```